Business Card Design needed for logo design project

Our company needs a Business Card Design. Please refer to our original project in the link above.
Dorian Whitlock
Broker

W: Grandvistaestates.com
P: 214-555-0187
F: 267-555-0142
E: dorianwhitlock@ferncrestmail.com
A: North Dallas Office

Name Spelling update , sorry Dorian Whitlock card is double sided

```html
<!DOCTYPE html>
<html lang="en">
<head>
<meta charset="utf-8">
<title>Grandvista Estates Realty – Business Card</title>
<link rel="stylesheet" href="https://fonts.googleapis.com/css2?family=Libre+Baskerville:wght@400;700&family=Open+Sans:wght@400&display=swap">
<style>
  :root {
    --backdrop: #f1f1f1;
    --card-white: #fdfdfd;
    --navy: #2f4472;
    --gold: #b8925a;
    --green: #2fae6a;
    --ink: #1b1b1b;
    --shadow: rgba(0, 0, 0, 0.18);
  }
  * { margin: 0; padding: 0; box-sizing: border-box; }
  html, body {
    width: 1200px;
    height: 1036px;
    overflow: hidden;
    background: var(--backdrop);
  }
  .sheet {
    position: relative;
    width: 1200px;
    height: 1036px;
  }
  .card {
    position: absolute;
    box-shadow: 0 14px 30px var(--shadow);
  }

  /* Contact side */
  .card-front {
    left: 50px;
    top: 341px;
    width: 620px;
    height: 354px;
    background: var(--card-white);
  }
  .front-name {
    position: absolute;
    left: 70px;
    top: 62px;
    font-family: "Libre Baskerville", Georgia, serif;
    font-weight: 700;
    font-size: 34px;
    color: var(--ink);
    letter-spacing: 0.2px;
  }
  .front-role {
    position: absolute;
    right: 60px;
    top: 104px;
    font-family: "Open Sans", Arial, sans-serif;
    font-size: 19px;
    color: var(--gold);
  }
  .front-rule {
    position: absolute;
    left: 70px;
    right: 60px;
    top: 136px;
    height: 2px;
    background: var(--green);
  }
  .front-contacts {
    position: absolute;
    right: 60px;
    top: 168px;
    list-style: none;
    text-align: right;
    font-family: "Open Sans", Arial, sans-serif;
    font-size: 20px;
    line-height: 1.36;
    color: var(--ink);
  }

  /* Brand side */
  .card-back {
    left: 710px;
    top: 133px;
    width: 440px;
    height: 770px;
    background: var(--navy);
    display: flex;
    flex-direction: column;
    align-items: center;
    justify-content: center;
    gap: 26px;
  }
  .brand-dot {
    width: 96px;
    height: 96px;
    border-radius: 50%;
    background: var(--gold);
  }
  .brand-name {
    font-family: "Libre Baskerville", Georgia, serif;
    font-weight: 400;
    font-size: 30px;
    line-height: 1.3;
    color: var(--gold);
    text-align: center;
    text-transform: uppercase;
    letter-spacing: 1px;
  }
</style>
</head>
<body>
  <main class="sheet">
    <section class="card card-front" aria-label="Contact side">
      <h1 class="front-name">Dorian Whitlock</h1>
      <p class="front-role">broker</p>
      <div class="front-rule"></div>
      <ul class="front-contacts">
        <li>P: 214-555-0187</li>
        <li>F: 267-555-0142</li>
        <li>E: dorianwhitlock@ferncrestmail.com</li>
        <li>W: Grandvistaestates.com</li>
      </ul>
    </section>

    <section class="card card-back" aria-label="Brand side">
      <div class="brand-dot"></div>
      <p class="brand-name">Grandvista<br>Estates Realty</p>
    </section>
  </main>
</body>
</html>
```